We are a General Practice - Family medicine
We also have Allied Health professionals working within our team

Industry/Entity Type

Business

Contact Information for Business Card

Front of the card to display:

HARBOURVIEW MEDICAL
PHONE 6381 2947

5/14 Kellerton Avenue
Launceston Tasmania 7268

Back of the card to display:

My Appointments
Date:
Time:
With:

Please remember to phone us on 6381 2947 to cancel your appointment if you can't keep it.
A fee applied to missed appointments

```html
<!DOCTYPE html>
<html lang="en">
<head>
<meta charset="UTF-8">
<title>Harbourview Medical – Appointment Card</title>
<link href="https://fonts.googleapis.com/css2?family=Arimo:wght@400&display=swap" rel="stylesheet">
<style>
  :root {
    --stage: #000000;
    --card: #ffffff;
    --cyan: #1ff0ff;
    --green: #93f226;
    --brand-blue: #4cc9f0;
    --brand-green: #8fdc2a;
  }
  * { margin: 0; padding: 0; box-sizing: border-box; }
  html, body {
    width: 1200px;
    height: 742px;
    overflow: hidden;
    background: var(--stage);
  }
  .stage {
    position: relative;
    width: 1200px;
    height: 742px;
    background: var(--stage);
    font-family: "Arimo", Arial, sans-serif;
  }
  .card {
    position: absolute;
    top: 219px;
    width: 519px;
    height: 303px;
    background: var(--card);
  }
  .card--front { left: 41px; }
  .card--back { left: 640px; }

  .front-contact {
    position: absolute;
    top: 19px;
    left: 367px;
    width: 140px;
    text-align: center;
    font-size: 16px;
    line-height: 18px;
  }
  .front-contact .practice-name { color: var(--cyan); }
  .front-contact .practice-phone { color: var(--green); }

  .brand {
    position: absolute;
    left: 30px;
    top: 178px;
    display: flex;
    align-items: center;
    gap: 10px;
  }
  .brand-dot {
    width: 34px;
    height: 34px;
    border-radius: 50%;
    background: var(--brand-green);
  }
  .brand-name {
    font-size: 28px;
    color: var(--brand-blue);
    letter-spacing: -0.3px;
  }

  .front-address {
    position: absolute;
    left: 20px;
    top: 279px;
    font-size: 14px;
    color: var(--cyan);
    white-space: nowrap;
  }

  .appointments-title {
    position: absolute;
    top: 23px;
    left: 0;
    width: 100%;
    text-align: center;
    font-size: 16px;
    color: var(--cyan);
  }
  .appointment-fields {
    position: absolute;
    left: 153px;
    top: 69px;
    list-style: none;
    font-size: 16px;
    color: var(--green);
  }
  .appointment-fields li { height: 36px; }

  .cancel-note {
    position: absolute;
    left: 0;
    top: 271px;
    width: 100%;
    text-align: center;
    font-size: 11.3px;
    color: var(--cyan);
    white-space: nowrap;
  }
</style>
</head>
<body>
<main class="stage">
  <section class="card card--front" aria-label="Card front">
    <div class="front-contact">
      <p class="practice-name">Harbourview Medical</p>
      <p class="practice-phone">6381 2947</p>
    </div>
    <div class="brand">
      <span class="brand-dot" aria-hidden="true"></span>
      <span class="brand-name">Harbourview Medical</span>
    </div>
    <p class="front-address">5/14 Kellerton Avenue Launceston Tasmania 7268</p>
  </section>

  <section class="card card--back" aria-label="Card back">
    <h1 class="appointments-title" style="font-weight:400">My Appointments</h1>
    <ul class="appointment-fields">
      <li>Date -</li>
      <li>Time -</li>
      <li>With -</li>
    </ul>
    <p class="cancel-note">Please remember to phone us on 6381 2947 to cancel your appointmentif you Can't keep it</p>
  </section>
</main>
</body>
</html>
```